Accounting firm needs a flyer "TREV Partners".. many job after this Stationary, business card

We need a flyer for a new company based in Melbourne Australia. We are group of young professionals who intend to provide various accounting services, taxation, finance, bookkeeping and payroll, Business service service advisory and management consulting.The main task of the firm is to provide accounting and taxation services. we then use our associates/referral partners to assist client with their legal, migration, finance needs.

We would like to see designs that match our logo, business card and letter head which I have uploaded along with this. I have also uploaded some of our website contents that might be used in flyers.
My favorite colors are: Blue (navy and royal blue), Teal (blue green), Turquoise, purple(orchid, lavender, plum).

Our brand:
TREV Partners
Where advice mean more

Our mission:
To group the professionals in house, where advice mean more and turn into better business for our people, for our clients and four our communities.

We like our logo, however we are still not sure about our business card. So if we are open to work with someone who works with flyers and business card at the same time .

Target Market(s)

Individual and business client in Australia

Industry/Entity Type

Finance And Accounting

Colors
0255a3
3176b5
0493ce
33a6d7
886aae
b768aa
00a990
33b8a4

Requirements
Must have
• TREV Partners logo
• Liability limited by a scheme approved under the professional standards legislation
• Our motto: TREV Partners where counsel goes further
• Short description of our services:
• • Bookkeeping & Payroll
• • Finance & Capital Raising
• • Taxation, Accounting and compliances
• • Business service and advisory
• • Migration
• • ASIC and Corporate Secretarial
• • Business law and legal services
• About us
• TREV aim to be more than just an accounting firm. We support our clients to help them achieve their personal and business goals by offering a fully integrated advisory service, helping clients to build wealth and protect their assets.We will bring together the relevant professionals across a number of specialties and locations; providing a responsive, personalised solution.
• Our mission: To group the professionals in house, where advice mean more and turn into better business for our people, for our clients and four our communities.
Nice to have
• Tax agent logo
• NCB logo

```html
<!DOCTYPE html>
<html lang="en">
<head>
<meta charset="utf-8">
<title>TREV Partners Flyer</title>
<link href="https://fonts.googleapis.com/css2?family=Barlow:wght@400;500;600&display=swap" rel="stylesheet">
<style>
  :root{
    --backdrop:#1c1c1c;
    --paper:#ffffff;
    --navy:#13286b;
    --royal:#0255a3;
    --teal:#00a990;
    --plum:#a1568f;
    --text:#3a3a3a;
    --rule:#b9b9b9;
    --photo-a:#c9d3dc;
    --photo-b:#e9edf1;
    --photo-c:#5a6470;
    --badge-green:#9bc43b;
    --badge-purple:#7b4ea0;
  }
  *{box-sizing:border-box;margin:0;padding:0}
  html,body{width:1200px;height:1000px;overflow:hidden}
  body{background:var(--backdrop);font-family:"Barlow",Arial,sans-serif;position:relative}
  .flyer{position:absolute;left:249px;top:47px;width:702px;height:906px;background:var(--paper);box-shadow:0 0 18px rgba(0,0,0,.6)}
  .accent-top{position:absolute;left:0;top:13px;width:301px;height:12px;background:var(--plum);clip-path:polygon(0 0,292px 0,100% 100%,0 100%)}
  .hero{position:absolute;left:0;top:25px;width:702px;height:284px;
    background:linear-gradient(135deg,var(--photo-c) 0%,var(--photo-a) 30%,var(--photo-b) 55%,var(--photo-a) 80%,var(--photo-c) 100%)}
  .accent-hero{position:absolute;right:0;top:308px;width:151px;height:15px;background:var(--teal);clip-path:polygon(0 0,100% 0,100% 100%,12px 100%)}
  .brand{position:absolute;left:42px;top:58px;text-align:center;width:92px}
  .brand-dot{width:90px;height:90px;border-radius:50%;background:var(--royal);margin:0 auto 6px}
  .brand-name{font-size:22px;font-weight:600;color:var(--royal);letter-spacing:1px}
  .col{position:absolute;width:290px;color:var(--text);font-size:12.5px;line-height:16px;letter-spacing:-0.15px}
  .col-left{left:44px;top:327px}
  .col-right{left:371px;top:336px}
  h2{font-size:15px;font-weight:600;color:var(--navy);display:flex;align-items:center;gap:6px;margin-bottom:8px;letter-spacing:0}
  h2::after{content:"";flex:0 0 168px;height:1px;background:var(--rule)}
  .block{margin-bottom:16px}
  .values{color:var(--navy);font-weight:500;margin-bottom:16px}
  .services-head{margin-bottom:4px}
  .service{text-align:justify;margin-bottom:16px}
  .service-title{color:var(--navy);font-weight:500}
  .service-title::before{content:"";display:inline-block;width:6px;height:6px;background:var(--teal);margin:0 5px 2px 1px}
  .badges{position:absolute;left:373px;top:798px;display:flex;gap:32px;align-items:center}
  .badge-round{width:50px;height:50px;border-radius:50%;background:var(--badge-green);border:3px solid #222}
  .badge-square{width:62px;height:40px;background:var(--badge-purple);border-radius:6px}
  .footer{position:absolute;left:0;bottom:0;width:702px;height:47px;background:var(--navy);color:#fff;
    display:flex;justify-content:center;align-items:center;gap:22px;font-size:14px;font-weight:600}
  .footer span{display:flex;align-items:center;gap:5px}
</style>
</head>
<body>
<div class="flyer">
  <div class="accent-top"></div>
  <div class="hero" role="img" aria-label="Photo of business people working with a calculator, pens and financial charts on a desk"></div>
  <div class="accent-hero"></div>
  <div class="brand">
    <div class="brand-dot"></div>
    <div class="brand-name">TREV</div>
  </div>

  <div class="col col-left">
    <div class="block">
      <h2>Our Mission:</h2>
      <p>To group the professionals in house, whereadvice mean more and turn into better business for our people, for our clients and four our communities.</p>
    </div>
    <div class="block">
      <h2>Our Firm:</h2>
      <p>As a group of professionals, our firm are available to provide you with high quality accounting, taxation and business advisory whether you are a business owner, family or an individual client.We have a strategic alliance with our referral lawyers, migration agents and mortgage brokers.</p>
    </div>
    <p class="values">Our core values include expertise, confidentiality, teamwork and commitment.</p>
    <h2 class="services-head">Our Services:</h2>
    <p class="service"><span class="service-title">Bookkeeping &amp; Payroll</span> Our bookkeeping involves maintaining accurate and updated records of all your business and personal financial activates. We manage your payroll on an ongoing basis, ensuring that all employees are compensated according to their employment agreements.</p>
    <p class="service"><span class="service-title">Finance &amp; Capital Raising</span> We regularly review client portfolios to identify opportunities and refer them to experienced and professional finance brokers to save and assist them with renegotiating a better deal with their current lender or seek out a better loan from a different lender.</p>
  </div>

  <div class="col col-right">
    <p class="service"><span class="service-title">Taxation, Accounting and Compliances</span> At TREV experienced tax agent build close working relationships with you to understand your circumstances and develop customised solutions for your personal income tax and corporate tax exposure.</p>
    <p class="service"><span class="service-title">Business Services and Advisory</span> While we provide peace of mind though takign care of the usual accounting and tax compliance matters, our real value lies in seeking to help you address business challenges and uncover opportunities.</p>
    <p class="service"><span class="service-title">Migration</span> The business Innovation visa or Employer Business Sponsored visa application can be complex with the requirement to submit various business, financial and asset documents.</p>
    <p class="service"><span class="service-title">ASIC and Corporate Secretarial</span> TREV understand that your corporate register, minutes and officeholder information and other secretarial register must kept for the life of the entity. Therefore, we maintain these documents.</p>
    <p class="service"><span class="service-title">Business law and legal services</span> When it comes to business law and legal services, you want to ensure you have a trusted competent legal team to work alongside with your accountants to help you across the broad range of commercial circumstances</p>
  </div>

  <div class="badges">
    <div class="badge-round" role="img" aria-label="Registered tax agent badge"></div>
    <div class="badge-square" role="img" aria-label="NCB member badge"></div>
  </div>

  <div class="footer">
    <span><svg width="13" height="11" viewBox="0 0 13 11"><rect x="0.5" y="0.5" width="12" height="10" fill="none" stroke="#fff"/><path d="M0.5 0.5 L6.5 6 L12.5 0.5" fill="none" stroke="#fff"/></svg>hello@trevpartners.com.au</span>
    <span><svg width="12" height="12" viewBox="0 0 12 12"><circle cx="6" cy="6" r="5.3" fill="none" stroke="#fff"/><ellipse cx="6" cy="6" rx="2.4" ry="5.3" fill="none" stroke="#fff"/><path d="M0.7 6 H11.3" stroke="#fff"/></svg>www.trevpartners.com.au</span>
    <span><svg width="12" height="12" viewBox="0 0 12 12"><circle cx="6" cy="6" r="5.3" fill="none" stroke="#fff"/><path d="M4 3 L5 5 L4.5 6 Q5.5 7.5 6 7.5 L7 7 L9 8" fill="none" stroke="#fff"/></svg>0491 570 312</span>
  </div>
</div>
</body>
</html>
```